Tom Verlane

I am the director of Casa Del Humo International. We make premium cigars

I want an insanely beautiful card that directly attracts attention. Do your best. The card can use emboss, foil, laser-cut metal or anything else. Make it stand out, but also elegant.

Target Market(s)

Cigar Distributors

Industry/Entity Type

Cigars

Contact Information for Business Card

Email: tom.verlane@verlanos.com + Logos (attached) + Position: Director + 'High-End Cigars'

Colors

Designer to choose colors to be used in the design.

Requirements
Nice to have
• Please check us out at www.casadelhumo.com and try to use our colors and styles

```html
<!DOCTYPE html>
<html lang="en">
<head>
<meta charset="utf-8">
<title>Casa Del Humo International – Business Card</title>
<link rel="stylesheet" href="https://fonts.googleapis.com/css2?family=EB+Garamond:wght@400;600;700&family=Arimo:wght@400&display=swap">
<style>
  :root {
    --backdrop: #d3d6d7;
    --paper: #f6f6f5;
    --ink: #2b2b2b;
    --crimson: #b3121b;
    --umber: #4a2a1c;
    --serif: "EB Garamond", Georgia, serif;
    --sans: "Arimo", Arial, sans-serif;
  }
  * { box-sizing: border-box; margin: 0; padding: 0; }
  html, body { width: 1200px; height: 829px; overflow: hidden; background: var(--backdrop); }
  .stage { position: relative; width: 1200px; height: 829px; }

  .card {
    position: absolute;
    top: 262px;
    width: 525px;
    height: 300px;
    background: var(--paper);
    box-shadow: 0 4px 0 var(--crimson), 0 18px 30px rgba(0,0,0,.18);
    overflow: hidden;
  }
  .card--front { left: 50px; }
  .card--back { left: 625px; }

  /* front */
  .holder { position: absolute; left: 36px; top: 48px; }
  .holder__name { font-family: var(--serif); font-weight: 700; font-size: 25px; color: var(--crimson); letter-spacing: .5px; line-height: 1; }
  .holder__role { font-family: var(--sans); font-size: 13px; color: var(--ink); margin-top: 4px; }
  .front-rule { position: absolute; left: 36px; top: 108px; width: 400px; height: 1px; background: var(--crimson); }
  .contacts { position: absolute; left: 36px; top: 120px; list-style: none; font-family: var(--sans); font-size: 12.5px; color: var(--ink); }
  .contacts li { display: flex; align-items: center; gap: 7px; height: 20px; }
  .contacts svg { width: 10px; height: 10px; fill: var(--crimson); }

  .house { position: absolute; text-align: center; }
  .house--small { right: 24px; top: 40px; width: 252px; }
  .house__name { font-family: var(--serif); font-weight: 400; color: var(--ink); white-space: nowrap; letter-spacing: .3px; }
  .house--small .house__name { font-size: 14.5px; }
  .house__rule { position: relative; height: 1px; background: var(--crimson); margin-top: 3px; }
  .house__rule::after { content: ""; position: absolute; left: 50%; top: -3px; width: 7px; height: 7px; background: var(--crimson); transform: translateX(-50%) rotate(45deg); }
  .house__place { font-family: var(--sans); color: var(--ink); text-align: center; margin-top: 6px; letter-spacing: .3px; }
  .house--small .house__place { font-size: 9px; }

  /* back */
  .house--large { left: 36px; right: 36px; top: 34px; }
  .house--large .house__name { font-size: 26px; }
  .house--large .house__place { font-size: 14px; padding-left: 60px; }
  .brand { position: absolute; left: 40px; top: 140px; font-family: var(--serif); font-weight: 700; font-size: 26px; color: var(--crimson); }
  .series { position: absolute; left: 330px; top: 212px; font-family: var(--serif); font-weight: 400; font-size: 24px; color: var(--umber); }
</style>
</head>
<body>
<main class="stage">
  <section class="card card--front" aria-label="Business card front">
    <div class="holder">
      <h1 class="holder__name">TOM VERLANE</h1>
      <p class="holder__role">Director + 'High-End Cigars</p>
    </div>
    <div class="front-rule"></div>
    <ul class="contacts">
      <li><svg viewBox="0 0 10 10"><path d="M2 0.5l2 2-1 1.2c.6 1.3 1.6 2.3 2.9 2.9l1.2-1 2 2-1.2 1.9C4.3 9.3.7 5.7.2 2z"/></svg>(555)-214-0386</li>
      <li><svg viewBox="0 0 10 10"><path d="M0 2h10v6H0z"/><path d="M.6 2.6l4.4 3 4.4-3" fill="none" stroke="#fff" stroke-width=".8"/></svg>tom.verlane@verlanos.com</li>
      <li><svg viewBox="0 0 10 10"><circle cx="5" cy="5" r="5"/></svg>www.casadelhumo.com</li>
    </ul>
    <div class="house house--small">
      <p class="house__name">CASA del HUMO INTERNATIONAL</p>
      <div class="house__rule"></div>
      <p class="house__place">CATACAMAS - HONDURAS</p>
    </div>
  </section>

  <section class="card card--back" aria-label="Business card back">
    <div class="house house--large">
      <p class="house__name">CASA del HUMO INTERNATIONAL</p>
      <div class="house__rule"></div>
      <p class="house__place">CATACAMAS - HONDURAS</p>
    </div>
    <p class="brand">Marinero</p>
    <p class="series">Serie Carmín</p>
  </section>
</main>
</body>
</html>
```